Tolvane - online store for farm produce

Online store selling fresh produce (vegetables, fruits, dairy products, meat, ...) from various farmers. Every farm has its own shopping window - order page - just like a really simple web store.

Please check the attached design brief and mock-ups for further details.

Target Market(s)

People looking for fresh vegetables, fruit, meat, ... delivered from farms

Industry/Entity Type

Farming

Coding

Coded - Design and coding required

Number of Pages Required

5+ page

Font styles to use
Sans Serif

Requirements
Must have
• Custom design. Good UX/UI design, very functional.
Responsive using bootstrap 12 point grid system

```html
<!DOCTYPE html>
<html lang="en">
<head>
<meta charset="utf-8">
<title>Tolvane – Fresh produce from the farm</title>
<link rel="stylesheet" href="https://fonts.googleapis.com/css2?family=Quicksand:wght@500;600;700&family=Rubik:wght@500;600&family=Roboto:wght@400;500&display=swap">
<style>
:root{
  --green:#8bc12a;
  --ink:#2e3136;
  --text:#55595e;
  --muted:#f7f7f7;
  --footer:#363a40;
  --white:#ffffff;
}
*{box-sizing:border-box;margin:0;padding:0}
html,body{width:1200px;height:2351px;overflow:hidden}
body{position:relative;background:var(--white);font-family:'Quicksand',sans-serif;color:var(--text)}
.abs{position:absolute}
.brand{font-family:'Quicksand',sans-serif;font-weight:700;font-size:38px;letter-spacing:-.5px;line-height:1}
.site-header{left:0;top:0;width:1200px;height:80px;background:var(--white)}
.site-header .brand{left:88px;top:22px;color:var(--ink)}
.nav a{position:absolute;top:33px;font-family:'Roboto',sans-serif;font-weight:500;font-size:11.5px;color:var(--ink);text-decoration:none;letter-spacing:.2px}
.nav a.active{color:var(--green)}
.account{left:935px;top:24px;width:33px;height:33px;border:1.5px solid var(--green);border-radius:50%}
.cart{left:984px;top:24px;width:128px;height:32px;border-radius:16px;background:var(--green);color:var(--white);font-family:'Roboto',sans-serif;font-weight:500;font-size:11.5px;display:flex;align-items:center;justify-content:center;gap:8px}
.btn{position:absolute;display:flex;align-items:center;justify-content:center;border-radius:17px;font-family:'Roboto',sans-serif;font-weight:500;font-size:11.5px;letter-spacing:.2px;border:1.5px solid var(--green);color:var(--green);background:var(--white)}
.btn.solid{background:var(--green);color:var(--white)}
.btn.ghost{background:transparent}
.photo{position:absolute}
.hero{left:0;top:80px;width:1200px;height:400px}
.hero-panel{left:0;top:0;width:352px;height:400px;background:var(--green)}
.hero-photo{left:352px;top:0;width:848px;height:400px;background:radial-gradient(ellipse at 55% 45%,#f2a93b 0%,#d88a35 35%,#6b4522 75%,#2e1e12 100%)}
.hero h1{position:absolute;left:88px;top:104px;font-family:'Rubik',sans-serif;font-weight:600;font-size:28px;color:var(--white);letter-spacing:.3px}
.hero p{position:absolute;left:88px;top:154px;width:460px;font-size:13.5px;line-height:19.2px;color:var(--white);font-weight:500}
h2.section-title{position:absolute;font-family:'Rubik',sans-serif;font-weight:600;font-size:23px;color:var(--ink);letter-spacing:.4px}
h2.section-title span{color:var(--green)}
.ticks{position:absolute;list-style:none}
.ticks li{display:flex;align-items:center;gap:10px;height:28.7px;font-size:15.5px;font-weight:500;color:var(--text)}
.ticks svg{flex:none}
.products{left:0;top:1279px;width:1200px;height:535px;background:var(--muted)}
.card{position:absolute;top:114px;width:232px;height:296px;background:var(--white);text-align:center}
.card.active{border:1.5px solid var(--green)}
.card .pic{position:absolute;left:46px;top:22px;width:140px;height:108px;border-radius:50%}
.card .rule{position:absolute;left:92px;top:157px;width:48px;height:3px;background:var(--green)}
.card h3{position:absolute;left:0;top:196px;width:100%;font-family:'Roboto',sans-serif;font-weight:400;font-size:12px;line-height:19.5px;color:var(--ink)}
.card .price{position:absolute;left:0;top:246px;width:100%;font-family:'Roboto',sans-serif;font-size:11px;color:var(--text)}
.card .price b{font-size:18px;font-weight:500;color:var(--green);margin-right:3px}
.card .actions{position:absolute;left:58px;top:70px;display:flex;gap:8px}
.card .actions span{width:31px;height:31px;border-radius:50%;background:var(--ink);display:flex;align-items:center;justify-content:center}
.card .actions span:first-child{background:var(--green)}
.arrow{position:absolute;top:256px;width:32px;height:32px;border-radius:50%;border:1.5px solid var(--green);display:flex;align-items:center;justify-content:center}
.site-footer{left:0;top:1814px;width:1200px;height:537px;background:var(--footer);color:#e4e6e8}
.site-footer .brand{left:88px;top:70px;color:var(--white)}
.site-footer h4{position:absolute;left:88px;top:124px;font-family:'Rubik',sans-serif;font-weight:500;font-size:19px;color:var(--white);letter-spacing:.3px}
.farm{position:absolute;left:88px;width:260px}
.farm h5{font-family:'Rubik',sans-serif;font-weight:500;font-size:15.5px;color:var(--green);margin-bottom:6px}
.farm p{font-size:13px;line-height:15.5px;font-weight:500;color:#e4e6e8}
.map{left:400px;top:65px;width:711px;height:375px;background:linear-gradient(120deg,#eef1f5 0%,#e6eaf0 55%,#c9ced6 100%)}
.copyright{position:absolute;left:88px;top:480px;font-size:12.5px;font-weight:500}
.copyright span{color:var(--green)}
.social{position:absolute;top:472px;width:32px;height:32px;border-radius:50%;border:1.5px solid var(--green)}
.social.on{background:var(--green)}
</style>
</head>
<body>

<header class="site-header abs">
  <div class="brand abs">Tolvane</div>
  <nav class="nav">
    <a class="active" style="left:624px">HOME</a>
    <a style="left:699px">CURRENT OFFERS</a>
    <a style="left:840px">SETTINGS</a>
  </nav>
  <div class="account abs">
    <svg width="30" height="30" viewBox="0 0 30 30"><circle cx="15" cy="12" r="3.6" fill="none" stroke="#8bc12a" stroke-width="1.3"/><path d="M9.5 21c.8-3.2 3-4.8 5.5-4.8s4.7 1.6 5.5 4.8" fill="none" stroke="#8bc12a" stroke-width="1.3"/></svg>
  </div>
  <div class="cart abs">
    <svg width="14" height="12" viewBox="0 0 14 12"><path d="M1 1h2l1.6 7h7l1.4-5H4" fill="none" stroke="#fff" stroke-width="1.3"/><circle cx="5.5" cy="10.5" r="1" fill="#fff"/><circle cx="10.5" cy="10.5" r="1" fill="#fff"/></svg>
    CART $0.00
  </div>
</header>

<section class="hero abs">
  <div class="hero-panel abs"></div>
  <div class="hero-photo photo" role="img" aria-label="Two farmers shaking hands in a field at sunset"></div>
  <h1>WHAT IS THIS ABOUT US</h1>
  <p>Lorem Ipsum is simply dummy text of the printing and typesetting industry. Lorem Ipsum has been the industry's standard It is a long established fact that a reader will be distracted by the readable content of a page when looking at its layout.</p>
  <div class="btn" style="left:88px;top:258px;width:144px;height:32px">PRODUCT SEARCH</div>
</section>

<section class="abs" style="left:0;top:480px;width:1200px;height:399px">
  <div class="photo" role="img" aria-label="Customer buying fresh vegetables at a market stall" style="left:0;top:0;width:600px;height:399px;background:linear-gradient(160deg,#c9b6ad 0%,#b95a4e 35%,#8a9a55 65%,#3f5a2c 100%)"></div>
  <h2 class="section-title" style="left:664px;top:78px">CUSTOMER <span>BENEFITS</span></h2>
  <ul class="ticks" style="left:664px;top:118px">
    <li><svg width="14" height="14" viewBox="0 0 14 14"><circle cx="7" cy="7" r="6" fill="none" stroke="#8bc12a" stroke-width="1.2"/><path d="M4.2 7.2l2 2 3.6-4" fill="none" stroke="#8bc12a" stroke-width="1.2"/></svg>Lorem Ipsum is simply dummy text of the printing</li>
    <li><svg width="14" height="14" viewBox="0 0 14 14"><circle cx="7" cy="7" r="6" fill="none" stroke="#8bc12a" stroke-width="1.2"/><path d="M4.2 7.2l2 2 3.6-4" fill="none" stroke="#8bc12a" stroke-width="1.2"/></svg>Readable content of a page when looking at its layout</li>
    <li><svg width="14" height="14" viewBox="0 0 14 14"><circle cx="7" cy="7" r="6" fill="none" stroke="#8bc12a" stroke-width="1.2"/><path d="M4.2 7.2l2 2 3.6-4" fill="none" stroke="#8bc12a" stroke-width="1.2"/></svg>Lorem Ipsum is simply dummy text of the printing</li>
    <li><svg width="14" height="14" viewBox="0 0 14 14"><circle cx="7" cy="7" r="6" fill="none" stroke="#8bc12a" stroke-width="1.2"/><path d="M4.2 7.2l2 2 3.6-4" fill="none" stroke="#8bc12a" stroke-width="1.2"/></svg>Readable content of a page when looking at its layout</li>
    <li><svg width="14" height="14" viewBox="0 0 14 14"><circle cx="7" cy="7" r="6" fill="none" stroke="#8bc12a" stroke-width="1.2"/><path d="M4.2 7.2l2 2 3.6-4" fill="none" stroke="#8bc12a" stroke-width="1.2"/></svg>Lorem Ipsum is simply dummy text of the printing</li>
  </ul>
  <div class="btn" style="left:664px;top:285px;width:145px;height:32px">PRODUCT SEARCH</div>
</section>

<section class="abs" style="left:0;top:879px;width:1200px;height:400px">
  <h2 class="section-title" style="left:88px;top:79px">FARMER <span>BENEFITS</span></h2>
  <ul class="ticks" style="left:88px;top:119px">
    <li><svg width="14" height="14" viewBox="0 0 14 14"><circle cx="7" cy="7" r="6" fill="none" stroke="#8bc12a" stroke-width="1.2"/><path d="M4.2 7.2l2 2 3.6-4" fill="none" stroke="#8bc12a" stroke-width="1.2"/></svg>Lorem Ipsum is simply dummy text of the printing</li>
    <li><svg width="14" height="14" viewBox="0 0 14 14"><circle cx="7" cy="7" r="6" fill="none" stroke="#8bc12a" stroke-width="1.2"/><path d="M4.2 7.2l2 2 3.6-4" fill="none" stroke="#8bc12a" stroke-width="1.2"/></svg>Readable content of a page when looking at its layout</li>
    <li><svg width="14" height="14" viewBox="0 0 14 14"><circle cx="7" cy="7" r="6" fill="none" stroke="#8bc12a" stroke-width="1.2"/><path d="M4.2 7.2l2 2 3.6-4" fill="none" stroke="#8bc12a" stroke-width="1.2"/></svg>Lorem Ipsum is simply dummy text of the printing</li>
    <li><svg width="14" height="14" viewBox="0 0 14 14"><circle cx="7" cy="7" r="6" fill="none" stroke="#8bc12a" stroke-width="1.2"/><path d="M4.2 7.2l2 2 3.6-4" fill="none" stroke="#8bc12a" stroke-width="1.2"/></svg>Readable content of a page when looking at its layout</li>
    <li><svg width="14" height="14" viewBox="0 0 14 14"><circle cx="7" cy="7" r="6" fill="none" stroke="#8bc12a" stroke-width="1.2"/><path d="M4.2 7.2l2 2 3.6-4" fill="none" stroke="#8bc12a" stroke-width="1.2"/></svg>Lorem Ipsum is simply dummy text of the printing</li>
  </ul>
  <div class="btn solid" style="left:88px;top:286px;width:145px;height:32px">TELL ME MORE</div>
  <div class="photo" role="img" aria-label="Farmer carrying a basket of fresh vegetables in a meadow" style="left:600px;top:0;width:600px;height:400px;background:linear-gradient(170deg,#e4e6df 0%,#c9d3b2 40%,#a8b96d 70%,#7e9a45 100%)"></div>
</section>

<section class="products abs">
  <h2 class="section-title" style="left:0;top:62px;width:1200px;text-align:center">FEATURED <span>PRODUCTS</span></h2>

  <div class="arrow" style="left:72px"><svg width="10" height="10" viewBox="0 0 10 10"><path d="M6.5 1.5L3 5l3.5 3.5" fill="none" stroke="#8bc12a" stroke-width="1.3"/></svg></div>
  <div class="arrow" style="left:1095px"><svg width="10" height="10" viewBox="0 0 10 10"><path d="M3.5 1.5L7 5 3.5 8.5" fill="none" stroke="#8bc12a" stroke-width="1.3"/></svg></div>

  <article class="card" style="left:88px">
    <div class="pic" role="img" aria-label="Kiwi fruit, whole and halved" style="background:radial-gradient(circle at 40% 55%,#9fd13a 0%,#6f9a2a 45%,#8a6a3a 75%,transparent 76%)"></div>
    <div class="rule"></div>
    <h3>CURABITUR VOLUTPAT NULLA<br>NON SEM CONGUE</h3>
    <div class="price"><b>€2</b>/ 1 KG</div>
  </article>

  <article class="card" style="left:352px">
    <div class="pic" role="img" aria-label="Ripe red tomatoes" style="background:radial-gradient(circle at 50% 55%,#f0553a 0%,#d8321f 55%,transparent 72%)"></div>
    <div class="rule"></div>
    <h3>CURABITUR VOLUTPAT NULLA<br>NON SEM CONGUE</h3>
    <div class="price"><b>€4</b>/ 2 KG</div>
  </article>

  <article class="card active" style="left:616px">
    <div class="pic" role="img" aria-label="Fresh beetroot with leaves" style="background:radial-gradient(circle at 50% 60%,#b8375c 0%,#8e2443 40%,#c6dca0 62%,transparent 74%)"></div>
    <div class="actions">
      <span><svg width="13" height="11" viewBox="0 0 14 12"><path d="M1 1h2l1.6 7h7l1.4-5H4" fill="none" stroke="#fff" stroke-width="1.3"/><circle cx="5.5" cy="10.5" r="1" fill="#fff"/><circle cx="10.5" cy="10.5" r="1" fill="#fff"/></svg></span>
      <span><svg width="13" height="12" viewBox="0 0 14 12"><path d="M7 11S1 7.3 1 4.1A2.9 2.9 0 0 1 7 2.6 2.9 2.9 0 0 1 13 4.1C13 7.3 7 11 7 11z" fill="none" stroke="#8bc12a" stroke-width="1.3"/></svg></span>
      <span><svg width="14" height="10" viewBox="0 0 14 10"><path d="M1 5s2.4-4 6-4 6 4 6 4-2.4 4-6 4-6-4-6-4z" fill="none" stroke="#8bc12a" stroke-width="1.3"/><circle cx="7" cy="5" r="1.7" fill="#8bc12a"/></svg></span>
    </div>
    <div class="rule"></div>
    <h3>CURABITUR VOLUTPAT NULLA<br>NON SEM CONGUE</h3>
    <div class="price"><b>€2</b>/ 1 KG</div>
  </article>

  <article class="card" style="left:880px">
    <div class="pic" role="img" aria-label="Red onion, whole and halved" style="background:radial-gradient(circle at 50% 55%,#b86aa0 0%,#7d1f45 50%,transparent 70%)"></div>
    <div class="rule"></div>
    <h3>CURABITUR VOLUTPAT NULLA<br>NON SEM CONGUE</h3>
    <div class="price"><b>€2</b>/ 1 KG</div>
  </article>

  <div class="btn ghost" style="left:512px;top:442px;width:176px;height:32px">VIEW ALL PRODUCTS</div>
</section>

<footer class="site-footer abs">
  <div class="brand abs">Tolvane</div>
  <h4>FEATURED FARM</h4>
  <div class="farm" style="top:173px"><h5>Farm Name - 01</h5><p>4410 Meadowbrook Lane,<br>Hollisford ML 33537</p></div>
  <div class="farm" style="top:250px"><h5>Farm Name - 02</h5><p>4410 Meadowbrook Lane,<br>Hollisford ML 33537</p></div>
  <div class="farm" style="top:328px"><h5>Farm Name - 03</h5><p>4410 Meadowbrook Lane,<br>Hollisford ML 33537</p></div>
  <div class="btn ghost" style="left:88px;top:410px;width:113px;height:32px">OUR FARM</div>

  <div class="map photo" role="img" aria-label="Street map showing farm locations near the coast"></div>

  <p class="copyright">© 2020 <span>Tolvane</span>. All Rights Reseved</p>
  <div class="social" style="left:1003px" role="img" aria-label="Social profile"></div>
  <div class="social on" style="left:1042px" role="img" aria-label="Social profile"></div>
  <div class="social" style="left:1080px" role="img" aria-label="Social profile"></div>
</footer>

</body>
</html>
```